Business Card Design Project

We need a logo design for a new company based in Southern California called "Norvale Security Services, Inc." We install security and camera systems for homeowners and business, to protect their assets.
Updates

Project Deadline Extended
Reason: LOGO Design completes in eight days. Would like that design decided before we finish the business cards. Thanks...

Target Market(s)

Homeowners and business owners looking for additional protection of their assets.

Industry/Entity Type

Security

Font styles to use
Serif

Requirements
Must have
• Company Name
Office# 909-472-3615
Service# 909-472-3616
email: NorvaleSecurity@brimwell.net
address: 48620 Thorncrest Lane Rancho Cucamonga, CA 91704
Nice to have
• Serving Southern California

```html
<!DOCTYPE html>
<html lang="en">
<head>
<meta charset="utf-8">
<title>Norvale Security Services, Inc. – Business Card</title>
<link rel="stylesheet" href="https://fonts.googleapis.com/css2?family=Tinos&family=Arimo&display=swap">
<style>
  :root {
    --sky: #72c4e2;
    --sky-soft: #a9dcef;
    --ink: #111111;
    --rule: #1d2733;
    --accent-blue: #2b7cc0;
    --paper: #ffffff;
    --steel-light: #e6e8ea;
    --steel-dark: #8d9297;
  }
  html, body {
    margin: 0;
    padding: 0;
    overflow: hidden;
    background: var(--paper);
  }
  .card {
    position: relative;
    width: 1200px;
    height: 740px;
    background: var(--paper);
    overflow: hidden;
    font-family: "Tinos", "Times New Roman", serif;
    color: var(--ink);
  }
  .title-band {
    position: absolute;
    left: 0; top: 0;
    width: 1200px; height: 128px;
    background: var(--sky);
  }
  .company-name {
    position: absolute;
    left: 0; top: 22px;
    width: 1200px;
    margin: 0;
    text-align: center;
    font-weight: 400;
    font-size: 64px;
    line-height: 80px;
    white-space: nowrap;
  }
  .rule {
    position: absolute;
    left: 0;
    width: 1200px;
    height: 4px;
    background: var(--rule);
  }
  .rule-top { top: 138px; }
  .rule-bottom { top: 646px; }
  .market {
    position: absolute;
    right: 62px; top: 160px;
    margin: 0;
    font-family: "Arimo", Arial, sans-serif;
    font-variant: small-caps;
    font-size: 56px;
    line-height: 64px;
    color: var(--accent-blue);
    letter-spacing: 1px;
  }
  .market-bar {
    position: absolute;
    left: 560px; top: 234px;
    width: 640px; height: 14px;
    background: linear-gradient(to right, rgba(114,196,226,0), var(--sky-soft) 25%, var(--sky));
  }
  .camera-art {
    position: absolute;
    left: 53px; top: 196px;
    width: 258px; height: 216px;
    border-radius: 22px;
    background: linear-gradient(160deg, var(--steel-light), var(--steel-dark));
  }
  .phones {
    position: absolute;
    left: 336px; top: 282px;
    margin: 0;
    font-size: 50px;
    line-height: 68px;
  }
  .contact {
    position: absolute;
    left: 0; top: 446px;
    width: 1200px;
    margin: 0;
    font-style: normal;
    font-size: 43px;
    line-height: 60px;
  }
  .contact span { display: block; white-space: nowrap; }
  .contact .email { padding-left: 178px; }
  .contact .street { padding-left: 62px; }
  .contact .city { padding-left: 252px; }
  .service-band {
    position: absolute;
    left: 0; top: 658px;
    width: 1200px; height: 66px;
    background: var(--sky);
  }
  .service-area {
    position: absolute;
    left: 0; top: 658px;
    width: 1200px;
    margin: 0;
    text-align: center;
    font-family: "Arimo", Arial, sans-serif;
    font-size: 46px;
    line-height: 66px;
    letter-spacing: 14.5px;
    color: var(--paper);
    white-space: nowrap;
  }
</style>
</head>
<body>
  <main class="card">
    <div class="title-band"></div>
    <h1 class="company-name">Norvale Security Services, Inc.</h1>
    <div class="rule rule-top"></div>

    <p class="market">Homes &amp; Business</p>
    <div class="market-bar"></div>

    <svg class="camera-art" role="img" aria-label="Illustration of a wall-mounted security camera" viewBox="0 0 258 216"></svg>

    <p class="phones">
      Office: 909-472-3615<br>
      Service: 909-472-3616
    </p>

    <address class="contact">
      <span class="email">Email: NorvaleSecurity@brimwell.net</span>
      <span class="street">Address: 48620 Thorncrest Lane Rancho Cucamonga,</span>
      <span class="city">CA 91704</span>
    </address>

    <div class="rule rule-bottom"></div>
    <div class="service-band"></div>
    <p class="service-area">Serving Southern California</p>
  </main>
</body>
</html>
```